Management Consultancy needs sharp professional services showcased in a brochure

We are a management consultancy specializing on contract management and conflict avoidance services requiring a professional brochure showcasing our services to prospective clients.

Attached are a selection of existing stationary and the colour scheme.

Further details on our company can be found at www.velto-advisory-partners.com
Updates

Preference is for bi-fold, however, innovative tri-fold will be considered. Added Monday, August 7, 2017

Target Market(s)

Construction companies, consultants, developers, oil and gas service providers, NGO's, SME's.

Industry/Entity Type

Management

Requirements
Must have
• High degree of professionalism with eye catching, sharp detail. No frils.
• Colour scheme as per the attachments
• Font as per attachments - Century Gothic
• Details of our company and services
Nice to have
• Open to ideas, thinking along the lines of a car brochure type design.
• Bi-fold preferred, by trifold accepted if innovative.
Should not have
• Remove reference to the United Arab Emirates.
• No cartoon/clipart photos.

```html
<!DOCTYPE html>
<html lang="en">
<head>
<meta charset="utf-8">
<title>Velto Consult – Tri-fold Brochure</title>
<link rel="stylesheet" href="https://fonts.googleapis.com/css2?family=Mulish:wght@400;600;700;800&family=Quattrocento:wght@400;700&display=swap">
<style>
  :root {
    --navy: #1b2d4f;
    --red: #b5121b;
    --ink: #222428;
    --paper: #ffffff;
    --backdrop: #d8d9db;
    --photo-dark: #1c1c1c;
    --photo-mid: #7a7a7a;
    --photo-light: #e6e8ea;
    --body-font: "Mulish", "Century Gothic", sans-serif;
    --serif-font: "Quattrocento", serif;
  }
  * { box-sizing: border-box; margin: 0; padding: 0; }
  html, body {
    width: 1200px; height: 1200px; overflow: hidden;
    background: var(--backdrop);
    font-family: var(--body-font);
    color: var(--ink);
  }
  .brochure {
    position: absolute; left: 30px; top: 165px;
    width: 1140px; height: 870px;
    display: flex;
    box-shadow: 0 6px 18px rgba(0,0,0,0.18);
  }
  .panel {
    position: relative; width: 380px; height: 870px;
    background: var(--paper); overflow: hidden;
  }
  .panel svg.art { position: absolute; left: 0; top: 0; width: 380px; height: 870px; }

  /* Services panel */
  .services { position: absolute; left: 38px; top: 490px; width: 304px; }
  .services h2 { color: var(--navy); font-size: 17px; font-weight: 700; margin-bottom: 14px; }
  .services p {
    font-size: 11px; line-height: 1.47; text-align: justify;
    margin-bottom: 14px; hyphens: auto;
  }

  /* Contact panel */
  .contact-panel { background: linear-gradient(180deg, #cfd1d4 0%, #e9eaec 45%, #f7f7f8 65%, #ffffff 100%); }
  .contact { position: absolute; left: 0; top: 600px; width: 380px; text-align: center; }
  .contact h2 {
    color: var(--red); font-size: 19px; font-weight: 800;
    text-decoration: underline; text-underline-offset: 4px; letter-spacing: 0.3px;
  }
  .contact .icon { display: block; margin: 0 auto; width: 22px; height: 22px; }
  .contact .phone-icon { margin-top: 26px; }
  .contact .phone { font-size: 27px; font-weight: 800; margin-top: 8px; letter-spacing: 0.5px; }
  .contact .mail-icon { margin-top: 14px; }
  .contact .email { font-size: 15px; font-weight: 700; margin-top: 10px; }
  .contact .web-icon { margin-top: 18px; }
  .contact .web { font-size: 12px; font-weight: 700; margin-top: 14px; }

  /* Cover panel */
  .cover-name {
    position: absolute; left: 0; top: 620px; width: 380px; text-align: center;
    font-family: var(--serif-font); font-weight: 400; color: var(--navy);
    font-size: 27px; letter-spacing: 1px;
  }
  .cover-name .mark {
    display: block; width: 14px; height: 14px; margin: 0 auto 10px;
    border-radius: 50%; background: var(--navy);
  }
  .tagline {
    position: absolute; left: 0; top: 705px; width: 380px; text-align: center;
    font-family: var(--serif-font); color: var(--navy); font-size: 28px;
  }
  .headline {
    position: absolute; left: 0; top: 738px; width: 380px; text-align: center;
    color: var(--red); font-weight: 800; font-size: 50px; letter-spacing: 1px;
  }
  .web-band {
    position: absolute; left: 0; top: 833px; width: 380px; height: 30px;
    background: var(--navy); color: #fff; text-align: center;
    font-size: 11px; font-weight: 700; letter-spacing: 3px; line-height: 30px;
  }
</style>
</head>
<body>
<main class="brochure">

  <section class="panel services-panel">
    <svg class="art" viewBox="0 0 380 870">
      <defs>
        <radialGradient id="bulbs" cx="0.7" cy="0.35" r="0.8">
          <stop offset="0" stop-color="#9a9a9a"/>
          <stop offset="0.5" stop-color="#3a3a3a"/>
          <stop offset="1" stop-color="var(--photo-dark)"/>
        </radialGradient>
      </defs>
      <path d="M0,0 H380 V100 Q340,450 0,472 Z" fill="var(--navy)"/>
      <path d="M0,0 H380 V80 Q336,432 0,454 Z" fill="var(--red)"/>
      <path d="M0,0 H380 V60 Q330,412 0,436 Z" fill="url(#bulbs)" role="img" aria-label="Photo of a row of light bulbs with one lit bulb"/>
    </svg>
    <div class="services">
      <h2>Our Services:</h2>
      <p>Every contract has at least two parties; every party has a goal, and every goal matters. Each party must work in equilibrium as a contractual partnership or alliance, it is on this premise we aim to deliver truly mutual agreements, maintaining the contract integrity from inception through the contract life, and where we are not party to the original agreement, we provide effective solutions to contractual conflict via our unique mediation methodology at all positions of the conflict cycle and aim to enhance all aspects of contract performance by effective audit and management.</p>
      <p>We believe that a proactive approach to contract management creates transparency and trust, and maintains relationships and builds on them for the future whilst cultivating significant value to your business transactions and addressing real and relevant issues, providing and implementing effective solutions. We believe that avoidance of contractual conflict and timely resolution on escalation is paramount in the effectiveness of any agreement.</p>
    </div>
  </section>

  <section class="panel contact-panel">
    <svg class="art" viewBox="0 0 380 870">
      <rect x="0" y="0" width="380" height="560" fill="#d2d4d7" opacity="0.35" role="img" aria-label="Soft-focus photo of colleagues reviewing documents"/>
      <path d="M8,0 Q110,340 380,490" fill="none" stroke="var(--navy)" stroke-width="16"/>
      <path d="M40,0 Q150,315 380,462" fill="none" stroke="var(--red)" stroke-width="16"/>
      <circle cx="190" cy="330" r="104" fill="#e4e5e7" stroke="var(--navy)" stroke-width="5" role="img" aria-label="Street map showing the office location"/>
    </svg>
    <div class="contact">
      <h2>CONTACT US</h2>
      <svg class="icon phone-icon" viewBox="0 0 22 22" aria-hidden="true">
        <circle cx="11" cy="11" r="11" fill="var(--navy)"/>
        <path d="M7.5,5.5 l2,0 l0.8,3 l-1.3,1 q1,2.2 3,3.2 l1,-1.3 l3,0.8 l0,2 q-0.5,1.3 -2,1.3 q-7,-1 -8,-8 q0,-1.5 1.5,-2z" fill="#fff"/>
      </svg>
      <div class="phone">555-014-2287</div>
      <svg class="icon mail-icon" viewBox="0 0 22 22" aria-hidden="true">
        <circle cx="11" cy="11" r="11" fill="var(--navy)"/>
        <rect x="5.5" y="7" width="11" height="8" fill="none" stroke="#fff" stroke-width="1.4"/>
        <path d="M5.5,7 L11,11.5 L16.5,7" fill="none" stroke="#fff" stroke-width="1.4"/>
      </svg>
      <div class="email">info@velto-advisory-partners.com</div>
      <svg class="icon web-icon" viewBox="0 0 22 22" aria-hidden="true">
        <circle cx="11" cy="11" r="11" fill="var(--navy)"/>
        <circle cx="11" cy="11" r="6" fill="none" stroke="#fff" stroke-width="1.3"/>
        <ellipse cx="11" cy="11" rx="2.6" ry="6" fill="none" stroke="#fff" stroke-width="1.2"/>
        <path d="M5,11 H17 M6,8 H16 M6,14 H16" stroke="#fff" stroke-width="1"/>
      </svg>
      <div class="web">www.velto-advisory-partners.com</div>
    </div>
  </section>

  <section class="panel cover-panel">
    <svg class="art" viewBox="0 0 380 870">
      <defs>
        <linearGradient id="portrait" x1="0" y1="0" x2="0" y2="1">
          <stop offset="0" stop-color="var(--photo-light)"/>
          <stop offset="0.6" stop-color="#a9adb3"/>
          <stop offset="1" stop-color="#4a4d54"/>
        </linearGradient>
      </defs>
      <path d="M0,0 H380 V478 Q190,560 0,505 Z" fill="var(--navy)"/>
      <path d="M0,0 H380 V470 Q190,550 0,496 Z" fill="var(--red)"/>
      <path d="M0,0 H380 V462 Q190,540 0,486 Z" fill="url(#portrait)" role="img" aria-label="Photo of a smiling businesswoman in a grey suit with a colleague behind her"/>
    </svg>
    <div class="cover-name"><span class="mark"></span>VELTO CONSULT</div>
    <div class="tagline">The Contract &amp; Conflict</div>
    <div class="headline">ADVISORY</div>
    <div class="web-band">www.velto-advisory-partners.com</div>
  </section>

</main>
</body>
</html>
```